Looking for something sharp classy and with an edge for an advanced civil construction business
Something that says professional
nothing too DARK

Target Market(s)

mining companies council civil contractors concrete works

Industry/Entity Type

Construction

Contact Information for Business Card

Brindle Civil Constructions
brindlecivilconstruction@quokkamail.com
Tavi Marlowe
0418275936

Font styles to use
Serif
Sans Serif

Colors
0455a3
0592cd
85cae6
000000
919191

Requirements
Must have
• On the back of the card must have
down the bottom small print email logo phone number

Should not have
• follow us on facebook
Brindle Civil Constructions

follow us on instagram
BRINDLECIVILCONSTRUCTIONS

```html
<!DOCTYPE html>
<html lang="en">
<head>
<meta charset="utf-8">
<title>Brindle Civil Constructions – Business Card</title>
<link href="https://fonts.googleapis.com/css2?family=Oswald:wght@500&family=Poppins:wght@400;500&display=swap" rel="stylesheet">
<style>
  :root {
    --backdrop: #e6e6ec;
    --card: #ffffff;
    --navy: #2e2d6b;
    --violet: #5756a6;
    --violet-deep: #3f3e86;
    --ink: #2b2b35;
    --muted: #55556a;
    --white: #ffffff;
  }
  * { margin: 0; padding: 0; box-sizing: border-box; }
  html, body {
    width: 1200px; height: 864px; overflow: hidden;
    background: var(--backdrop);
    font-family: "Poppins", Arial, sans-serif;
  }
  .stage {
    position: relative; width: 1200px; height: 864px;
    display: flex; align-items: center; justify-content: center; gap: 40px;
  }
  .card {
    position: relative; width: 560px; height: 320px;
    background: var(--card);
    box-shadow: 0 10px 30px rgba(30, 30, 60, 0.18);
    overflow: hidden;
  }
  .brand {
    position: absolute; display: flex; align-items: center; gap: 12px;
    color: var(--navy); font-family: "Poppins", Arial, sans-serif; font-weight: 500;
    white-space: nowrap;
  }
  .brand-mark { background: var(--navy); flex: none; }
  .card-front .brand { left: 50%; top: 50%; transform: translate(-50%, -50%); font-size: 24px; }
  .card-front .brand-mark { width: 22px; height: 22px; }
  .card-back .brand { right: 28px; top: 104px; font-size: 18px; gap: 10px; }
  .card-back .brand-mark { width: 16px; height: 16px; }

  .band { position: absolute; left: 0; top: 0; width: 560px; height: 320px; }
  .address {
    position: absolute; left: 312px; top: 238px;
    color: var(--white); font-size: 12.5px; letter-spacing: 0.2px;
    white-space: nowrap;
  }
  .person { position: absolute; left: 30px; top: 132px; }
  .person-name {
    font-family: "Oswald", Arial, sans-serif; font-weight: 500;
    font-size: 21px; color: var(--navy); letter-spacing: 0.5px; text-transform: uppercase;
  }
  .person-title {
    font-size: 9.5px; color: var(--ink); letter-spacing: 1px; text-transform: uppercase; margin-top: 1px;
  }
  .contacts { position: absolute; left: 30px; top: 186px; list-style: none; }
  .contacts li {
    display: flex; align-items: center; gap: 8px;
    font-size: 9.5px; color: var(--muted); height: 17px; white-space: nowrap;
  }
  .contacts svg { width: 10px; height: 10px; fill: var(--ink); flex: none; }
</style>
</head>
<body>
<main class="stage">
  <section class="card card-front" aria-label="Card front">
    <div class="brand"><span class="brand-mark"></span>Brindle Civil Constructions</div>
  </section>

  <section class="card card-back" aria-label="Card back">
    <svg class="band" viewBox="0 0 560 320" aria-hidden="true">
      <defs>
        <linearGradient id="bandFill" x1="0" y1="0" x2="1" y2="0">
          <stop offset="0" stop-color="#3f3e86"/>
          <stop offset="1" stop-color="#5d5cab"/>
        </linearGradient>
      </defs>
      <path d="M0,296 L248,296 Q266,296 270,279 L278,226 Q282,209 300,209 L560,209"
            fill="none" stroke="#2e2d6b" stroke-width="2.5"/>
      <path d="M0,320 L0,302 L252,302 Q270,302 274,285 L282,232 Q286,215 304,215 L560,215 L560,320 Z"
            fill="url(#bandFill)"/>
    </svg>

    <div class="brand"><span class="brand-mark"></span>Brindle Civil Constructions</div>

    <div class="person">
      <div class="person-name">Tavi Marlowe</div>
      <div class="person-title">General Manager</div>
    </div>

    <ul class="contacts">
      <li><svg viewBox="0 0 10 10"><path d="M2 0.5 L3.6 0.5 L4.3 2.8 L3.2 3.7 Q4 5.6 6.3 6.8 L7.2 5.7 L9.5 6.4 L9.5 8 Q9.5 9.5 8 9.5 Q0.5 9 0.5 2 Q0.5 0.5 2 0.5Z"/></svg>0418 275 936</li>
      <li><svg viewBox="0 0 10 10"><path d="M2.5 0 H7.5 V10 H2.5Z M3.3 1 V8 H6.7 V1Z"/></svg>0418 275 936</li>
      <li><svg viewBox="0 0 10 10"><path d="M2.5 0 H7.5 V3 H2.5Z M0.5 3.5 H9.5 V8 H0.5Z M2.5 7 H7.5 V10 H2.5Z"/></svg>0418 275 936</li>
      <li><svg viewBox="0 0 10 10"><path d="M0.5 2 H9.5 V8.5 H0.5Z M1.2 2.6 L5 5.6 L8.8 2.6" stroke="#fff" stroke-width="0.8"/></svg>brindlecivilconstruction@quokkamail.com</li>
      <li><svg viewBox="0 0 10 10"><circle cx="5" cy="5" r="4.5"/><path d="M0.5 5 H9.5 M5 0.5 Q2 5 5 9.5 Q8 5 5 0.5" stroke="#fff" stroke-width="0.7" fill="none"/></svg>www.brindlecivil.com.au</li>
    </ul>

    <p class="address">42 Quarry Lane, Kalgoorlie WA</p>
  </section>
</main>
</body>
</html>
```